Erstellung eines responsiven One-Pagers für mittelständiges Unternehmen im Bauhauptgewerbe
Zielgruppe
Seit fast 30 Jahren sind wir als mittelständiges Unternehmen im Bauhauptgewerbe tätig.
Aufgabenstellung
Die bestehende Webseite soll einen Relaunch bekommen. Dazu entnehmen Sie bitte Bildmaterial und Logo aus der alten Seite. Wir würden gerne daraus einen responsiven One-Pager bauen.
Da die alte Seite jetzt schon 10 Jahre alt ist, würden wir gerne ein neues Design erstellen lassen. Später werden wir es entweder selbst von unserem Programmierer entwickeln lassen oder Sie erstellen uns ein Angebot. Das Design sollte auch so aufgebaut sein, dass es responsive funktionieren würde.

```html
<!DOCTYPE html>
<html lang="de">
<head>
<meta charset="utf-8">
<title>Kaltenbach Bauwerkserhalt</title>
<link href="https://fonts.googleapis.com/css2?family=Open+Sans:ital,wght@0,300;0,400;0,600;0,700;1,300&family=Fira+Sans+Condensed:wght@400;500&display=swap" rel="stylesheet">
<style>
:root{
  --navy:#13294b;
  --blue:#2a56a5;
  --blue-mid:#2f5dab;
  --blue-light:#5b82c4;
  --accent:#1f66b8;
  --text:#333;
  --grey:#7a7a7a;
  --white:#fff;
}
*{box-sizing:border-box;margin:0;padding:0}
html,body{width:1200px;height:2344px;overflow:hidden}
body{font-family:"Open Sans",Arial,sans-serif;color:var(--text);background:var(--white);position:relative}
.abs{position:absolute}
.cond{font-family:"Fira Sans Condensed","Arial Narrow",sans-serif}

.topbar{left:0;top:0;width:1200px;height:27px;background:linear-gradient(90deg,#fff 55%,#e6e6e6);font-size:11px;color:#333}
.topbar .claim{position:absolute;left:103px;top:7px}
.topbar .legal{position:absolute;right:82px;top:7px}

.header{left:0;top:27px;width:1200px;height:84px;background:var(--white)}
.brand{position:absolute;left:103px;top:28px;display:flex;align-items:center;gap:10px}
.brand .square{width:22px;height:22px;background:var(--blue)}
.brand .name{font-size:20px;font-weight:600;color:var(--blue);line-height:1}
.contact-item{position:absolute;top:22px;display:flex;gap:7px}
.contact-item svg{flex:none;margin-top:2px}
.contact-item b{display:block;color:var(--accent);font-size:15px;font-weight:700;line-height:18px}
.contact-item span{display:block;color:var(--grey);font-size:13px;font-weight:300;line-height:18px}

.nav{left:0;top:111px;width:1200px;height:44px;background:var(--blue)}
.nav .dark{position:absolute;right:0;top:0;width:300px;height:44px;background:var(--navy);clip-path:polygon(30px 0,100% 0,100% 100%,0 100%)}
.nav ul{position:absolute;left:100px;top:0;display:flex;list-style:none;height:44px;align-items:center;color:var(--white);font-size:14px}
.nav li{padding:0 10px}
.nav li.sep{padding:0 2px}
.nav li.active{background:var(--navy);font-weight:700;height:44px;line-height:44px;padding:0 14px}
.nav .social{position:absolute;right:82px;top:12px;width:20px;height:20px;background:var(--white);border-radius:2px}

.hero{left:0;top:155px;width:1200px;height:386px;background:linear-gradient(180deg,#8a95a3 0%,#b8bec6 45%,#7d848c 100%)}
.hero-title{left:0;top:50px;width:1200px;text-align:center;color:var(--white);text-shadow:0 2px 6px rgba(0,0,0,.55)}
.hero-title .l1{font-size:52px;font-weight:300;line-height:58px}
.hero-title .l2{font-size:58px;font-weight:700;line-height:64px}
.hero-title .tag{font-size:17px;margin-top:10px}
.btn-hero{top:221px;width:168px;height:45px;border-radius:23px;color:var(--white);font-size:19px;text-align:center;line-height:45px}
.dot{left:1104px;width:16px;height:16px;border-radius:50%;background:rgba(255,255,255,.9)}

.cards{left:100px;top:484px;width:1019px;height:183px;display:flex}
.card{height:183px;padding:15px 25px;color:var(--white)}
.card h2{font-size:30px;font-weight:300;line-height:34px;margin-bottom:10px}
.card p,.card li{font-size:11px;font-weight:300;line-height:14px}
.card ul{list-style:none}
.card li::before{content:"✔ ";font-weight:700}
.card .pill{display:inline-block;margin-top:10px;background:var(--white);color:var(--blue);font-size:10px;padding:4px 12px;border-radius:12px}
.card strong{display:block;font-size:14px;font-weight:600;line-height:17px;margin-bottom:12px}

.sec-title{left:0;width:1200px;text-align:center;font-size:31px;font-weight:300;color:#222}
.sec-sub{left:0;width:1200px;text-align:center;font-size:15px;color:var(--accent);letter-spacing:.3px}
.sec-rule{left:566px;width:68px;height:3px;background:var(--accent)}
.sec-text{left:245px;width:740px;text-align:center;font-size:10.5px;font-style:italic;font-weight:300;color:var(--grey);line-height:14px}

.band{left:0;top:914px;width:1200px;height:46px;background:var(--navy);color:var(--white);text-align:center;font-size:30px;font-weight:300;line-height:44px}
.svc-photo{left:0;top:960px;width:605px;height:378px;background:linear-gradient(135deg,#9fb0c2,#cfc9bd 50%,#8f8a80)}
.svc-tab{left:412px;width:193px;background:var(--blue);color:var(--white);font-size:12px;line-height:14px;padding:6px 10px 6px 26px;position:absolute}
.svc-tab::before{content:"✔";position:absolute;left:11px;top:6px;font-weight:700}
.svc-tab.active{background:var(--navy)}
.svc-body{left:605px;top:960px;width:595px;height:378px;background:linear-gradient(90deg,#fff 30%,#d6d6d6)}
.svc-body h3{position:absolute;left:36px;top:20px;font-size:20px;font-weight:300;color:#444}
.svc-body h4{position:absolute;left:36px;top:57px;font-size:13px;font-weight:600;color:#555}
.svc-body p{position:absolute;left:36px;width:480px;font-size:11px;font-weight:300;color:var(--grey);line-height:13.6px}
.btn-small{position:absolute;background:var(--blue);color:var(--white);font-size:11px;text-align:center;border-radius:15px}
.thumb{top:1249px;height:46px;background:linear-gradient(135deg,#7f8f6d,#b7b9b0)}

.ref{top:1551px;height:133px}
.arrow{top:1596px}
.btn-ref{top:1708px;width:168px;height:35px;border-radius:18px;background:var(--blue);color:var(--white);font-size:13px;text-align:center;line-height:35px}

.contact{left:0;top:1787px;width:1200px;height:405px;background:linear-gradient(180deg,#e4e4e4,#f7f7f7 40%,#efefef)}
.circle{left:97px;top:1897px;width:252px;height:252px;border-radius:50%;background:linear-gradient(160deg,#c9d1dc,#f4f6f8 45%,#7f8a94)}
.c-lead{left:405px;top:1942px;width:340px;font-size:18px;font-weight:300;color:#555;line-height:21px}
.c-line{left:406px;display:flex;gap:7px;font-size:13px;color:#444;line-height:16px}
.field-label{left:781px;font-size:10px;color:var(--grey)}
.field{left:781px;width:339px;height:30px;background:var(--white);border:1px solid #e0e0e0}
.note{left:781px;top:2104px;font-size:7.5px;color:#555;line-height:11px}
.send{left:1022px;top:2103px;width:99px;height:24px;border-radius:12px;background:var(--blue);color:var(--white);text-align:center;font-size:15px;line-height:24px;letter-spacing:1px}

.footer{left:0;top:2192px;width:1200px;height:105px;background:var(--blue);color:var(--white)}
.footer .brand{left:100px;top:40px}
.footer .brand .square{background:var(--white)}
.footer .brand .name{color:var(--white);font-size:19px}
.f-head{position:absolute;font-size:17px;font-weight:300;border-bottom:1px solid var(--white);padding-bottom:1px}
.f-col{position:absolute;font-size:12.5px;font-weight:300;line-height:15px}
.f-nav{position:absolute;font-size:10px;line-height:12.5px;text-transform:uppercase}
.bottombar{left:0;top:2297px;width:1200px;height:47px;background:var(--navy);color:var(--white);text-align:center;font-size:13px;font-weight:300;line-height:47px}
</style>
</head>
<body>

<div class="abs topbar">
  <span class="claim">Seit über 20 Jahren: Betoninstandsetzung – Spritzbeton – Brückensanierung – Balkone – Abdichtung</span>
  <span class="legal">IMPRESSUM | DATENSCHUTZ</span>
</div>

<header class="abs header">
  <div class="brand"><div class="square"></div><div class="name">Kaltenbach Bauwerkserhalt</div></div>
  <div class="contact-item" style="left:510px">
    <svg width="20" height="28" viewBox="0 0 20 28"><path d="M10 1a8 8 0 0 0-8 8c0 6 8 17 8 17s8-11 8-17a8 8 0 0 0-8-8z" fill="none" stroke="#13294b" stroke-width="3"/><circle cx="10" cy="9" r="3" fill="#13294b"/></svg>
    <div><b>Besuchen Sie uns</b><span>Mühlbachweg 12, 68799 Lindenau</span></div>
  </div>
  <div class="contact-item" style="left:748px">
    <svg width="32" height="30" viewBox="0 0 32 30"><rect x="10" y="2" width="12" height="26" rx="2" fill="none" stroke="#13294b" stroke-width="2.5"/><path d="M6 10q-3 5 0 10M26 10q3 5 0 10" fill="none" stroke="#13294b" stroke-width="2"/></svg>
    <div><b>Rufen Sie an</b><span>(0 62 00) 41 17 20</span></div>
  </div>
  <div class="contact-item" style="left:922px">
    <svg width="42" height="30" viewBox="0 0 42 30"><rect x="1" y="3" width="40" height="25" fill="none" stroke="#13294b" stroke-width="2"/><path d="M1 3l20 14L41 3M1 28l15-12M41 28L26 16" fill="none" stroke="#13294b" stroke-width="2"/></svg>
    <div><b>Schreiben Sie uns</b><span>info@kaltenbach-bau.de</span></div>
  </div>
</header>

<nav class="abs nav">
  <div class="dark"></div>
  <ul>
    <li class="active">STARTSEITE</li><li>UNTERNEHMEN</li><li class="sep">|</li><li>LEISTUNGEN</li><li class="sep">|</li><li>REFERENZEN</li><li class="sep">|</li><li>KARRIERE</li><li class="sep">|</li><li>KONTAKT</li>
  </ul>
  <div class="social"></div>
</nav>

<section class="abs hero" role="img" aria-label="Foto der Firmenhalle mit Transportern und Mitarbeitern auf dem Hof">
  <div class="abs hero-title">
    <div class="l1">Willkommen bei</div>
    <div class="l2">Kaltenbach Bau</div>
    <div class="tag">Betoninstandsetzung - Spritzbeton - Brückensanierung - Balkone - Abdichtung</div>
  </div>
  <div class="abs btn-hero" style="left:449px;background:var(--navy)">ÜBER UNS</div>
  <div class="abs btn-hero" style="left:632px;background:var(--blue)">KONTAKT</div>
  <div class="abs dot" style="top:198px"></div>
  <div class="abs dot" style="top:218px;background:rgba(255,255,255,.7)"></div>
  <div class="abs dot" style="top:237px;background:rgba(255,255,255,.7)"></div>
</section>

<section class="abs cards">
  <div class="card" style="width:256px;background:var(--navy)">
    <h2>KONTAKT</h2>
    <p>Mühlbachweg 12<br>68799 Lindenau</p>
    <p style="margin-top:12px">Tel. (0 62 00) 41 17 20<br>Fax (0 62 00) 41 17 21<br>Mail: info@kaltenbach-bau.de</p>
  </div>
  <div class="card" style="width:254px;background:var(--blue)">
    <h2>LEISTUNGEN</h2>
    <ul><li>Brückensanierung &amp; Korrosionsschutz</li><li>Statische Spritzbetonverstärkungen</li><li>Beton- und Balkoninstandsetzung</li><li>Horizontalsperren, Beschichtung</li></ul>
    <span class="pill">ZU DEN LEISTUNGEN</span>
  </div>
  <div class="card" style="width:254px;background:var(--blue-mid)">
    <h2>ÜBER UNS</h2>
    <p>Als mittelständisches, überregional tätiges Unternehmen dürfen wir uns vorstellen. Wir sind Mitglied der Bau-berufsgenossenschaft in Karlsruhe.</p>
    <span class="pill" style="margin-top:20px">ZUM UNTERNEHMEN</span>
  </div>
  <div class="card" style="width:255px;background:var(--blue-light)">
    <h2>KARRIERE</h2>
    <strong>Vorarbeiter und Facharbeiter gesucht</strong>
    <p>für die Betonsanierung.<br>Ein Führerschein ist erforderlich.</p>
    <span class="pill" style="padding:4px 22px">ZU DEN JOBS</span>
  </div>
</section>

<h1 class="abs sec-title" style="top:700px;left:-26px">Betonsanierung in Heidelberg, Mannheim &amp; Umgebung</h1>
<div class="abs sec-sub cond" style="top:744px;left:-20px">LANGFRISTIGE BETONERHALTUNG DURCH INSTANDSETZUNG UND KORROSIONSSCHUTZ</div>
<div class="abs sec-rule" style="top:773px;left:590px"></div>
<p class="abs sec-text" style="top:794px;left:250px">Sie sind richtig bei uns wenn wir über folgende Begriffe sprechen: Betonschäden, Balkonschäden, Betonschutz- und Instandsetzung, Betonkosmetik, Betonsanierung, Balkone, Brücken, Brandschäden, SIVV, PCC, SPCC und Spritzbeton. Als Untergrundvorbereitung, bei jeder Instandhaltungs-maßnahme, ist eine Reinigung erforderlich. Hierbei kommt das Sandstrahlen, Druckluftstrahlen, Wasserstrahlen, Fräsen oder Schleifen zum Einsatz.</p>
<div class="abs" style="left:508px;top:848px;width:240px;height:28px;background:linear-gradient(90deg,transparent,#ececec 20%,#ececec 80%,transparent)" role="img" aria-label="Handschriftlicher Gruß: Wir freuen uns auf Sie"></div>

<h2 class="abs band">Unsere Leistungen</h2>
<div class="abs svc-photo" role="img" aria-label="Foto eines Mitarbeiters bei der Beschichtung einer Brückenfläche"></div>
<div class="svc-tab active" style="top:1036px;height:57px;padding-top:9px">Brückensanierung und<br>Korrosionsschutz</div>
<div class="svc-tab" style="top:1096px;height:48px">Statische Spritzbeton-<br>verstärkungen</div>
<div class="svc-tab" style="top:1148px;height:47px">Beton- und<br>Balkoninstandsetzung</div>
<div class="svc-tab" style="top:1199px;height:63px">Horizontalsperren,<br>Beschichtung,<br>Kellerabdichtung</div>
<div class="abs svc-body">
  <h3>Brückensanierung und Korrosionsschutz</h3>
  <h4>Brückensanierung</h4>
  <p style="top:80px">Brücken werden durch den zunehmenden Verkehr, besonders durch die Traglast von Lastwagen immer stärker beansprucht. Deshalb ist eine regelmäßige Kontrolle und Ausbesserung der Schäden unverzichtbar. Wir setzen mit unserer langjähriger Erfahrung Brücken kompetent in Stand oder erneuern sie bei Bedarf, um sie für die tägliche Be-anspruchung wieder tauglich und sicher zu machen.</p>
  <p style="top:161px;width:485px">Grundlage für die Instandsetzung von Brückenbauwerken ist die ZTV-ING. Hierbei handelt es sich um zusätzliche technische Vertragsbedingungen und Richtlinien für Ingenieurbauten, Stand: Dezember 2007. Alle verwendeten Produkte für die Ausführung werden geprüft und in der aktuellen BAST-Liste aufgeführt.</p>
  <div class="btn-small cond" style="left:386px;top:224px;width:128px;height:29px;line-height:29px">ERFAHREN SIE MEHR</div>
  <div style="position:absolute;left:38px;top:267px;font-size:13px;color:#555">Zur Vergrößerung anklicken:</div>
</div>
<div class="abs thumb" style="left:643px;width:86px" role="img" aria-label="Foto einer Brückentreppe"></div>
<div class="abs thumb" style="left:734px;width:75px;background:linear-gradient(135deg,#5a5a4e,#9a937f)" role="img" aria-label="Foto einer Brückenunterseite"></div>
<div class="abs thumb" style="left:814px;width:75px;background:linear-gradient(135deg,#6e7480,#a39a8b)" role="img" aria-label="Foto eines Brückenpfeilers"></div>
<div class="abs thumb" style="left:895px;width:75px" role="img" aria-label="Foto einer Treppe an einer Brücke"></div>

<h2 class="abs sec-title" style="top:1374px;left:26px">Referenzen</h2>
<div class="abs sec-sub cond" style="top:1418px;left:26px">GEHÖREN AUCH SIE DAZU</div>
<div class="abs sec-rule" style="top:1455px;left:592px"></div>
<p class="abs sec-text" style="top:1476px;left:245px">Wir führen Objekte in verschiedenen Größenordnung aus. Es werden auch Baustellen als Generalunternehmer ausgeführt. Hierbei arbeiten wir auss-chließlich mit langjährigen, zuverlässigen Partnern zusammen (Gerüstbau, Fliesen- Schlosser- Malerarbeiten). Anbei unter anderen folgende Objekte, um sich einen Überblick über unser umfassendes Leistungsspektrum zu verschaffen.</p>
<svg class="abs arrow" style="left:97px" width="20" height="32" viewBox="0 0 20 32"><path d="M16 3L4 16l12 13" fill="none" stroke="#2a56a5" stroke-width="5"/></svg>
<div class="abs ref" style="left:132px;width:224px;background:linear-gradient(180deg,#6f7782,#b9bcc0)" role="img" aria-label="Foto eines Hochhauses mit Gerüst"></div>
<div class="abs ref" style="left:374px;width:222px;background:linear-gradient(135deg,#4a4b3a,#a98f68 55%,#6c7f52)" role="img" aria-label="Foto einer Natursteinkuppel mit Gewölbeöffnung"></div>
<div class="abs ref" style="left:616px;width:221px;background:linear-gradient(180deg,#b5bcae,#9a9c8a 60%,#66704e)" role="img" aria-label="Foto einer Betonbrücke über einem Bach"></div>
<div class="abs ref" style="left:857px;top:1549px;width:222px;background:linear-gradient(180deg,#7f9ec9,#c9cbc8 60%,#e6e3dc)" role="img" aria-label="Foto eines Kirchengebäudes mit Kuppel"></div>
<svg class="abs arrow" style="left:1093px" width="20" height="32" viewBox="0 0 20 32"><path d="M4 3l12 13L4 29" fill="none" stroke="#2a56a5" stroke-width="5"/></svg>
<div class="abs btn-ref cond" style="left:455px">GEWERBLICHE OBJEKTE</div>
<div class="abs btn-ref cond" style="left:634px;top:1706px">PRIVATE OBJEKTE</div>

<section class="abs contact"></section>
<h2 class="abs sec-title" style="top:1815px;left:20px">Kontaktieren Sie uns</h2>
<div class="abs sec-sub cond" style="top:1860px;left:20px">MIT UNS HABEN SIE EINEN EXPERTEN GEFUNDEN</div>
<div class="abs sec-rule" style="top:1899px;left:585px"></div>
<div class="abs circle" role="img" aria-label="Foto eines Firmentransporters mit Beschriftung"></div>
<p class="abs c-lead">Vereinbaren Sie doch gleich mit uns ein kostenloses Erstgespräch.</p>
<div class="abs c-line" style="top:1993px">
  <svg width="14" height="18" viewBox="0 0 14 18"><path d="M7 1a5.5 5.5 0 0 0-5.5 5.5C1.5 11 7 17 7 17s5.5-6 5.5-10.5A5.5 5.5 0 0 0 7 1z" fill="none" stroke="#2a56a5" stroke-width="2"/><circle cx="7" cy="6.5" r="2" fill="#2a56a5"/></svg>
  <span>Kaltenbach Bauwerkserhalt<br>Mühlbachweg 12, 68799 Lindenau</span>
</div>
<div class="abs c-line" style="top:2033px">
  <svg width="14" height="18" viewBox="0 0 14 18"><rect x="2" y="1" width="10" height="16" rx="1.5" fill="none" stroke="#2a56a5" stroke-width="2"/></svg>
  <span>Tel. (0 62 00) 41 17 20</span>
</div>
<div class="abs c-line" style="top:2061px">
  <svg width="14" height="18" viewBox="0 0 14 18"><circle cx="7" cy="9" r="6" fill="none" stroke="#2a56a5" stroke-width="2"/><path d="M1 9h12M7 3v12" stroke="#2a56a5" stroke-width="1.2"/></svg>
  <span>kontakt@kaltenbach-bau.de</span>
</div>

<div class="abs field-label" style="top:1924px">&#9632; Ihr Name*</div>
<div class="abs field" style="top:1941px"></div>
<div class="abs field-label" style="top:1981px">&#9742; Telefonnummer*</div>
<div class="abs field" style="top:1998px"></div>
<div class="abs field-label" style="top:2040px">&#9632; Ihr Anliegen*</div>
<div class="abs field" style="top:2057px"></div>
<p class="abs note cond">Die mit * gekennzeichneten Felder sind Pflichtfelder.<br>Ihre Daten werden vertraulich behandelt.</p>
<div class="abs send">SENDEN</div>

<footer class="abs footer">
  <div class="brand"><div class="square"></div><div class="name">Kaltenbach Bauwerkserhalt</div></div>
  <div class="f-head" style="left:461px;top:13px;width:302px">KONTAKT</div>
  <div class="f-col" style="left:461px;top:42px">Kaltenbach Bauwerkserhalt<br>Mühlbachweg 12<br>68799 Lindenau</div>
  <div class="f-col" style="left:626px;top:42px">Tel (0 62 00) 41 17 20<br>Fax (0 62 00) 41 17 21<br>info@kaltenbach-bau.de</div>
  <div class="f-head" style="left:843px;top:13px;width:276px">NAVIGATION</div>
  <div class="f-nav" style="left:843px;top:44px"><b>Startseite</b><br>Unternehmen<br>Leistungen<br>Referenzen</div>
  <div class="f-nav" style="left:965px;top:44px">Karriere<br>Kontakt<br>Impressum<br>Datenschutz</div>
</footer>
<div class="abs bottombar">© Kaltenbach Bauwerkserhalt 2019</div>

</body>
</html>
```